"Tales of Quiet Harbors" Book Cover Design

I am seeking a dynamic, modern, and professional cover design for a book focused on groundbreaking science that explores how a supplement called plasmalogens can revitalize the brain, prevent Alzheimer’s, and safeguard memories. The design should strike a balance between being visually appealing and conveying the seriousness of the topic.

Target Market(s)

The target audience includes individuals who are curious about cutting-edge science and proactive approaches to brain health, as well as those seeking to better understand how to protect their cognitive functions and memories. The cover should resonate with readers interested in health, science, and self-improvement, while reflecting the book’s informative and empowering tone.

Requirements
Must have
• The quotation across the top of the page (this is a placeholder for now, it will be changed eventually) and the author's name.
Should not have
• You don't need to use the puzzle idea!

```html
<!DOCTYPE html>
<html lang="en">
<head>
<meta charset="utf-8">
<title>Tales of Quiet Harbors — Book Cover</title>
<link rel="stylesheet" href="https://fonts.googleapis.com/css2?family=Montserrat:wght@700;800;900&display=swap">
<style>
  :root {
    --paper: #f8f1f0;
    --teal: #237f84;
    --red: #c92b20;
    --green: #2f9a4a;
    --art-cool: #8fc3c4;
    --art-warm: #9fcb8a;
    --art-base: #e6b4a2;
  }
  * { margin: 0; padding: 0; box-sizing: border-box; }
  html, body {
    width: 905px;
    height: 1200px;
    overflow: hidden;
    background: var(--paper);
  }
  .cover {
    position: relative;
    width: 905px;
    height: 1200px;
    background: var(--paper);
    font-family: "Montserrat", sans-serif;
    color: var(--teal);
  }
  .endorsement {
    position: absolute;
    top: 80px;
    left: 0;
    width: 100%;
    text-align: center;
    font-weight: 800;
    line-height: 1.45;
  }
  .endorsement-quote { font-size: 16.5px; }
  .endorsement-source { font-size: 15px; }
  .title {
    position: absolute;
    left: 0;
    top: 0;
    width: 905px;
    height: 420px;
  }
  .title text {
    font-family: "Montserrat", sans-serif;
    font-weight: 900;
  }
  .title-line-1 { fill: var(--teal); }
  .title-line-2 { fill: var(--red); }
  .title-line-3, .title-initial { fill: var(--green); }
  .cover-illustration {
    position: absolute;
    left: 175px;
    top: 489px;
    width: 564px;
    height: 569px;
    background: linear-gradient(160deg, var(--art-cool) 0%, var(--art-warm) 55%, var(--art-base) 100%);
  }
  .author {
    position: absolute;
    top: 1090px;
    left: 0;
    width: 100%;
    text-align: center;
    font-size: 31px;
    font-weight: 900;
  }
</style>
</head>
<body>
  <main class="cover">
    <header class="endorsement">
      <p class="endorsement-quote">“An incredible guide to protecting your mind and memories”</p>
      <p class="endorsement-source">Dr. Lena Marsh, MD</p>
    </header>

    <svg class="title" viewBox="0 0 905 420" role="heading" aria-level="1" aria-label="Tales of Quiet Harbors">
      <text class="title-line-1" x="166" y="222" font-size="107" textLength="571" lengthAdjust="spacingAndGlyphs">TALES OF</text>
      <text class="title-line-2" x="166" y="299" font-size="97" textLength="368" lengthAdjust="spacingAndGlyphs">QUIET</text>
      <text class="title-line-3" x="166" y="406" font-size="104" textLength="368" lengthAdjust="spacingAndGlyphs">HARBOR</text>
      <text class="title-initial" x="555" y="406" font-size="250" textLength="184" lengthAdjust="spacingAndGlyphs">S</text>
    </svg>

    <div class="cover-illustration" role="img" aria-label="Cover illustration: an open head with a brain split between a cool teal half of office cubicles and a lush green half of people enjoying music, art and nature"></div>

    <p class="author">Adrian Holloway, MD</p>
  </main>
</body>
</html>
```